Business Card Design Needed for Landscaping & Trail Building Company

We need a business card for our landscaping and trail-building business using our current artwork (attached). We build mountain bike trails and pump tacks along with our base business - landscaping - which is primarily earth moving, machine work, concreting, retaining walls, paths, etc. for commercial and residential customers. We want a design that is professional, sleek, and earthy. We like clean, open space (i.e. logo artwork only, on one side, with pertinent information on the back) and a somewhat ambiguous look considering our varied clientele between the trail work and the landscape work.

Target Market(s)

Ski resort executives. government employees (rangers, council members, etc), average homeowner, other tradies, builders, etc.

Contact Information for Business Card

Must include the following:
employee name: Marcus
mobile number: 0491 637 215
email: marcus@brellowgrounds.com.au
website: brellowgrounds.com.au
ABN: 58 314 902 667
QBCC: 27846159
^This is the Queensland Building & Construction Commission license number, a requirement to be displayed on promotional material for our state
Description of services: "Residential and commercial landscaping, minor earth works and trail building"

Font styles to use
Serif

Colors
ffc214
9bcb3c
333333
0355a3

Requirements
Must have
• Please see "Business Card Details" as these are all the pieces of information required to be on there. This will be a slim card, so the final size needs to be 45mm x 90mm, landscape perspective.
• I will include the requirements of our printer below:
• File Format
• PDF files
• CMYK colour
• 300dpi resolution minimum
• Fonts converted to outlines or flattened
• Resolution
• Images such as photos in your artwork must have a minimum resolution of 300dpi. Images that have a lower resolution may print pixelated or fuzzy. Images taken from the internet often have a resolution of only 72dpi and will very rarely print very well.
• Correct Colour
• Digital printing uses a CMYK colour format (Cyan, Magenta, Yellow and Black). The colours on your screen are RGB colours (Red, Green, Blue).
• Some RGB colours that appear on your screen can not be printed in CMYK. You must be careful when selecting colours for your printing, as some colours will print "dull" when compared to your computer screen.
• Programs such as Adobe Photoshop and Adobe Illustrator can convert all colours to CMYK. Programs such as Microsoft Word can not, so you must manually select colours which are not at risk.
• Fonts
• You may choose to select only common fonts such as "Arial" and "Times New Roman", or you can "embed" the fonts when saving your artwork. Preferably fonts in your artwork need to be "converted to outlines" or "flattened" into a graphic. This will eliminate the chance of fonts not displaying correctly and not printing the way you intended.
• Business Card Artwork Size
• 94mm x 59mm (including 2mm bleed)
• Artwork Bleeds - IMPORTANT!
• Your artwork needs to be a certain size to print correctly. For business cards it is 94mmx59mm. Part of this size is what we call the "bleed" which will be trimmed off. The bleed area is 2mm on each side. In addition to the bleed area outside the cut line, we strongly recommend making another internal margin as the cut line can vary in location.
Nice to have
• We will have a print run of two designs, one with my details (Dianne) and one with Marcus's.
• (I like the idea of the name being larger than everything else, jumping out)
• The background colours we are interested in: very dark navy blue (almost black), fluorescent orange and green (same colour palette as our current artwork), and possibly black. The rest of the colour theming should match our current artwork. We will likely be printing these out in matte/soft finish with a gloss spot accent on the logo.
• I have attached the front/back of an example business card that we both like the look of.
• As a side note, we are open to creative designs that design outside of our specified preferences, as we have been blown away in the past by the creativity of designers.

```html
<!DOCTYPE html>
<html lang="en">
<head>
<meta charset="utf-8">
<title>Brellow Grounds – Business Card Options</title>
<link href="https://fonts.googleapis.com/css2?family=Arimo&family=Cinzel:wght@600&family=Tinos:wght@400;700&display=swap" rel="stylesheet">
<style>
  :root {
    --navy: #151a30;
    --charcoal: #3a3e42;
    --paper: #ffffff;
    --orange: #eea33a;
    --green: #8dc34a;
    --ink: #333333;
    --light: #ffffff;
    --rule: #c9c9c9;
  }
  * { margin: 0; padding: 0; box-sizing: border-box; }
  html, body { width: 1200px; height: 997px; overflow: hidden; background: var(--paper); }
  .sheet { position: relative; width: 1200px; height: 997px; }

  .label {
    position: absolute; font-family: "Arimo", sans-serif; font-size: 21px;
    color: #111; line-height: 1; transform: translateX(-50%);
  }
  .label--left { transform: none; }

  .card {
    position: absolute; width: 582px; height: 291px; overflow: hidden;
    color: var(--light);
  }
  .card--navy { background: var(--navy); }
  .card--charcoal { background: var(--charcoal); }
  .card--white { background: var(--paper); border: 1px solid #8a8a8a; color: var(--ink); }

  .brand-mark {
    position: absolute; border-radius: 50%; background: var(--green);
  }
  .brand-stack {
    position: absolute; left: 94px; top: 82px; width: 120px; text-align: center;
  }
  .brand-stack .brand-mark { position: static; display: block; width: 80px; height: 80px; margin: 0 auto 10px; }
  .brand-stack .brand-name {
    font-family: "Tinos", serif; font-weight: 700; font-size: 15px; color: var(--green); line-height: 1.1;
  }

  .front-brand {
    position: absolute; left: 62px; top: 88px; display: flex; align-items: center; gap: 18px;
  }
  .front-brand .brand-mark { position: static; width: 104px; height: 104px; }
  .front-brand .brand-name {
    font-family: "Tinos", serif; font-weight: 700; font-size: 46px; color: var(--green); white-space: nowrap;
  }

  .tagline {
    position: absolute; left: 0; right: 0; top: 222px; text-align: center;
    font-family: "Cinzel", serif; font-weight: 600; font-size: 17px; letter-spacing: 1.3px;
    color: var(--orange); line-height: 23px;
  }

  .divider { position: absolute; left: 241px; top: 70px; width: 1px; height: 135px; background: var(--rule); }
  .card--white .divider { background: #9a9a9a; }

  .contact { position: absolute; left: 274px; top: 70px; }
  .contact__name {
    font-family: "Tinos", serif; font-weight: 700; font-size: 35px; color: var(--orange);
    line-height: 40px; margin-bottom: 4px;
  }
  .contact__row {
    display: flex; align-items: center; gap: 10px;
    font-family: "Tinos", serif; font-size: 19.5px; line-height: 24.5px; white-space: nowrap;
  }
  .contact__row svg { width: 15px; height: 15px; flex: none; }

  .licences {
    position: absolute; font-family: "Tinos", serif; font-size: 12.5px; line-height: 15px;
  }
  .licences--bottom { left: 418px; top: 232px; }
  .licences--top { left: 30px; top: 26px; }
</style>
</head>
<body>
<svg width="0" height="0" style="position:absolute">
  <defs>
    <symbol id="icon-phone" viewBox="0 0 16 16">
      <rect x="4" y="1" width="8" height="14" rx="1.8" fill="none" stroke="#8dc34a" stroke-width="1.8"/>
      <rect x="6.5" y="11.5" width="3" height="1.5" fill="#8dc34a"/>
    </symbol>
    <symbol id="icon-mail" viewBox="0 0 16 16">
      <rect x="1" y="3.5" width="14" height="9" fill="#8dc34a"/>
      <path d="M1.5 4 L8 9 L14.5 4" fill="none" stroke="#fff" stroke-width="1.2"/>
    </symbol>
    <symbol id="icon-web" viewBox="0 0 16 16">
      <g fill="none" stroke="#8dc34a" stroke-width="1.4">
        <circle cx="8" cy="8" r="6.5"/>
        <ellipse cx="8" cy="8" rx="3" ry="6.5"/>
        <path d="M1.5 8 H14.5 M2.5 4.8 H13.5 M2.5 11.2 H13.5"/>
      </g>
    </symbol>
  </defs>
</svg>

<main class="sheet">
  <span class="label" style="left:292px; top:0;">Front</span>
  <span class="label" style="left:886px; top:0;">Option 1</span>
  <span class="label label--left" style="left:10px; top:339px;">Back</span>
  <span class="label" style="left:291px; top:339px;">Option 2</span>
  <span class="label" style="left:908px; top:339px;">Option 3</span>
  <span class="label" style="left:607px; top:680px;">Option 4</span>

  <!-- Front -->
  <section class="card card--navy" style="left:0; top:31px;">
    <div class="front-brand">
      <span class="brand-mark"></span>
      <span class="brand-name">Brellow Grounds</span>
    </div>
    <p class="tagline">Residential and commercial landscaping,<br>minor earth works and trail building</p>
  </section>

  <!-- Option 1 -->
  <section class="card card--navy" style="left:605px; top:31px;">
    <p class="licences licences--top">ABN: 58 314 902 667<br>QBCC: 27846159</p>
    <div class="brand-stack" style="top:66px;">
      <span class="brand-mark"></span>
      <span class="brand-name">Brellow Grounds</span>
    </div>
    <span class="divider" style="top:70px;"></span>
    <div class="contact" style="top:70px;">
      <p class="contact__name">Dianne</p>
      <p class="contact__row"><svg><use href="#icon-phone"/></svg>0491 637 215</p>
      <p class="contact__row"><svg><use href="#icon-mail"/></svg>dianne@brellowgrounds.com.au</p>
      <p class="contact__row"><svg><use href="#icon-web"/></svg>brellowgrounds.com.au</p>
    </div>
    <p class="tagline">Residential and commercial landscaping,<br>minor earth works and trail building</p>
  </section>

  <!-- Option 2 -->
  <section class="card card--charcoal" style="left:0; top:365px;">
    <div class="brand-stack">
      <span class="brand-mark"></span>
      <span class="brand-name">Brellow Grounds</span>
    </div>
    <span class="divider"></span>
    <div class="contact">
      <p class="contact__name">Marcus</p>
      <p class="contact__row"><svg><use href="#icon-phone"/></svg>0491 637 215</p>
      <p class="contact__row"><svg><use href="#icon-mail"/></svg>marcus@brellowgrounds.com.au</p>
      <p class="contact__row"><svg><use href="#icon-web"/></svg>brellowgrounds.com.au</p>
    </div>
    <p class="licences licences--bottom">ABN: 58 314 902 667<br>QBCC: 27846159</p>
  </section>

  <!-- Option 3 -->
  <section class="card card--white" style="left:616px; top:365px;">
    <div class="brand-stack">
      <span class="brand-mark"></span>
      <span class="brand-name">Brellow Grounds</span>
    </div>
    <span class="divider"></span>
    <div class="contact">
      <p class="contact__name">Marcus</p>
      <p class="contact__row"><svg><use href="#icon-phone"/></svg>0491 637 215</p>
      <p class="contact__row"><svg><use href="#icon-mail"/></svg>marcus@brellowgrounds.com.au</p>
      <p class="contact__row"><svg><use href="#icon-web"/></svg>brellowgrounds.com.au</p>
    </div>
    <p class="licences licences--bottom">ABN: 58 314 902 667<br>QBCC: 27846159</p>
  </section>

  <!-- Option 4 -->
  <section class="card card--navy" style="left:326px; top:705px;">
    <div class="brand-stack">
      <span class="brand-mark"></span>
      <span class="brand-name">Brellow Grounds</span>
    </div>
    <span class="divider"></span>
    <div class="contact">
      <p class="contact__name">Dianne</p>
      <p class="contact__row"><svg><use href="#icon-phone"/></svg>0491 637 215</p>
      <p class="contact__row"><svg><use href="#icon-mail"/></svg>dianne@brellowgrounds.com.au</p>
      <p class="contact__row"><svg><use href="#icon-web"/></svg>brellowgrounds.com.au</p>
    </div>
    <p class="licences licences--bottom">ABN: 58 314 902 667<br>QBCC: 27846159</p>
  </section>
</main>
</body>
</html>
```